(4) Bowling League Designs 1920x1080

Will be used on our website and in some digital signage.

We are starting (4) leagues this summer and need a basic graphic as an attention grab which will then lead the customer to full information / sign ups. The information I would need on each one is as follows:

1. Monday Night FREE ball league - Begins May 3rd

2. Tuesday Trios - KFDL Sanctioned - Begins May 11th
$9,000 prize fund

3. Wednesday Cosmic League - 9 pin no tap fun league - May 12th start

4. Thursday Night FREE ball league - Begins May 13th

I will attach some random examples of previous ones to give you an idea.

```html
<!DOCTYPE html>
<html lang="en">
<head>
<meta charset="utf-8">
<title>Thursday Night Free Ball League</title>
<link href="https://fonts.googleapis.com/css2?family=Bebas+Neue&display=swap" rel="stylesheet">
<style>
  :root {
    --text: #ffffff;
    --glow: rgba(255, 40, 40, 0.85);
    --warm: #e8765a;
    --amber: #d98a3c;
    --pink: #d24a6a;
    --deep: #5a0c14;
    --night: #1c0508;
  }
  html, body {
    margin: 0;
    padding: 0;
    overflow: hidden;
    background: var(--night);
  }
  .poster {
    position: relative;
    width: 1200px;
    height: 675px;
    overflow: hidden;
    font-family: "Bebas Neue", "Oswald", sans-serif;
    color: var(--text);
  }
  .scene {
    position: absolute;
    inset: 0;
    background:
      radial-gradient(ellipse 420px 480px at 1000px 420px, #7a1420 0%, var(--deep) 55%, transparent 80%),
      radial-gradient(ellipse 300px 200px at 250px 40px, rgba(255,120,80,0.8), transparent 70%),
      radial-gradient(ellipse 260px 160px at 580px 300px, rgba(180,190,220,0.45), transparent 70%),
      linear-gradient(180deg, var(--warm) 0%, var(--pink) 35%, #c25a3a 60%, var(--amber) 100%);
  }
  .scene::after {
    content: "";
    position: absolute;
    inset: 0;
    background: linear-gradient(90deg, transparent 0%, transparent 48%, rgba(40,6,10,0.6) 70%, rgba(28,5,8,0.85) 100%);
  }
  .headline,
  .start-date {
    position: absolute;
    margin: 0;
    line-height: 1;
    font-weight: 400;
    white-space: nowrap;
  }
  .headline {
    text-shadow: 0 0 6px var(--glow), 0 0 14px rgba(255,60,60,0.5);
  }
  .headline--day { left: 96px; top: 77px; font-size: 196px; }
  .headline--night { left: 99px; top: 246px; font-size: 196px; }
  .headline--league { left: 101px; top: 457px; font-size: 165px; letter-spacing: 1px; word-spacing: 6px; }
  .start-date {
    right: 38px;
    text-align: right;
    text-shadow: 0 0 6px rgba(0,0,0,0.45);
  }
  .start-date--label { top: 107px; font-size: 62px; letter-spacing: 25px; margin-right: -25px; }
  .start-date--day { top: 167px; font-size: 94px; }
  .next-arrow {
    position: absolute;
    left: 1078px;
    top: 500px;
    width: 80px;
    height: 72px;
  }
</style>
</head>
<body>
  <main class="poster">
    <div class="scene" role="img" aria-label="Blurred bowling alley with neon lights and a dark red bowling ball in the foreground"></div>

    <h1 class="headline headline--day">THURSDAY</h1>
    <p class="headline headline--night">NIGHT</p>
    <p class="headline headline--league">FREE BALL LEAGUE</p>

    <p class="start-date start-date--label">BEGINS</p>
    <p class="start-date start-date--day">MAY 13TH</p>

    <svg class="next-arrow" viewBox="0 0 80 72" aria-hidden="true">
      <polyline points="20,8 56,36 20,64" fill="none" stroke="#ffffff" stroke-width="12" stroke-linecap="round" stroke-linejoin="round"/>
    </svg>
  </main>
</body>
</html>
```